Wedding Invite for Same Sex Marriage

Looking for creative ideas for our wedding invite, then other cards/information to accompany the invite i.e RSVP, Info Card, Wishing Well.We're a same sex male couple. Our thoughts are something along the lines of the Tumbleweed cartoon series. We put something together quickly for our Save The Date attached. These were printed in various bright colours. Don't stick to this design, be creative with the theme.Love to see what ideas you have.

Font styles to use
Sans Serif
Decorative
Script

Colors

Designer to choose colors to be used in the design.

Requirements
Must have
• Standard details of our names, location and time
Nice to have
• Unsure, looking for ideas from a creative crowd. Probably standard print sizes
Should not have
• Traditional, not cutesy cartoon

```html
<!DOCTYPE html>
<html lang="en">
<head>
<meta charset="utf-8">
<title>Save The Date – Wedding Invitation Concept</title>
<link href="https://fonts.googleapis.com/css2?family=Righteous&family=Great+Vibes&family=Kaushan+Script&family=Noto+Serif:ital,wght@0,400;1,700&family=Questrial&display=swap" rel="stylesheet">
<style>
  :root {
    --page: #ffffff;
    --card: #050607;
    --lime: #97be32;
    --steel: #4a6585;
    --navy: #22304a;
    --plum: #a357a0;
    --amber: #f0a321;
    --date-ink: #fdf1e2;
    --rose: #e21d3c;
    --rose-soft: #f06a86;
    --suit: #3f4450;
    --suit-light: #b9c6ea;
    --white: #ffffff;
    --muted: #9a9ca4;
    --ink: #1b1b1b;
  }
  * { box-sizing: border-box; margin: 0; padding: 0; }
  html, body { width: 1200px; height: 1051px; overflow: hidden; background: var(--page); }
  .canvas { position: relative; width: 1200px; height: 1051px; }
  .card { position: absolute; left: 39px; top: 39px; width: 1123px; height: 815px; background: var(--card); }
  .block { position: absolute; }

  .groom-left-art { left: 59px; top: 59px; width: 241px; height: 515px;
    background: linear-gradient(180deg, #2c2f36 0%, var(--suit) 55%, #22252b 100%); border-radius: 6px; }
  .groom-right-art { left: 942px; top: 262px; width: 199px; height: 572px;
    background: linear-gradient(180deg, #6d7180 0%, var(--suit-light) 55%, #8f9cc4 100%); border-radius: 6px; }
  .couple-heart-art { left: 790px; top: 244px; width: 144px; height: 132px;
    background: radial-gradient(circle at 50% 45%, #f6dcc0 0%, #e9c8a6 60%, #d8b08a 100%); border-radius: 50% 50% 45% 45%; }
  .rose-art { left: 59px; top: 578px; width: 356px; height: 254px;
    background: radial-gradient(circle at 55% 55%, var(--rose-soft) 0%, var(--rose) 65%); }
  .rose-faint-art { left: 424px; top: 704px; width: 112px; height: 128px;
    background: radial-gradient(circle at 40% 60%, rgba(160,140,160,0.35) 0%, rgba(34,48,74,0) 70%); }

  .name-bar { background: var(--lime); display: flex; align-items: center; justify-content: center; }
  .name-bar--left { left: 303px; top: 59px; width: 112px; height: 512px; }
  .name-bar--right { left: 788px; top: 355px; width: 125px; height: 477px; }
  .name { font-family: "Righteous", sans-serif; color: var(--lime); -webkit-text-stroke: 2.5px var(--white);
    paint-order: stroke fill; writing-mode: vertical-rl; transform: rotate(180deg);
    text-transform: uppercase; white-space: nowrap; line-height: 1; }
  .name--left { font-size: 58px; letter-spacing: 5px; }
  .name--right { font-size: 48px; letter-spacing: 4px; }

  .headline { left: 424px; top: 59px; width: 355px; height: 116px; background: var(--steel);
    display: flex; flex-direction: column; align-items: center; justify-content: center; color: var(--white); }
  .headline__small { font-family: "Righteous", sans-serif; font-size: 21px; text-transform: uppercase;
    letter-spacing: 2px; line-height: 1; margin-bottom: 4px; }
  .headline__big { font-family: "Righteous", sans-serif; font-size: 60px; text-transform: uppercase;
    line-height: 1; letter-spacing: 3px; color: var(--steel); -webkit-text-stroke: 2.5px var(--white); }

  .save-date { left: 788px; top: 59px; width: 354px; height: 108px; background: var(--plum);
    display: flex; align-items: center; justify-content: center;
    font-family: "Kaushan Script", cursive; font-size: 50px; color: var(--white); }
  .date-band { left: 788px; top: 176px; width: 354px; height: 56px; background: var(--amber);
    display: flex; align-items: center; justify-content: center;
    font-family: "Righteous", sans-serif; font-size: 40px; color: var(--date-ink); letter-spacing: 4px; line-height: 1; }

  .panel { background: var(--navy); color: var(--white); text-align: center; font-family: "Noto Serif", serif; }
  .details { left: 424px; top: 184px; width: 355px; height: 387px; }
  .rsvp { left: 424px; top: 578px; width: 355px; height: 254px; }
  .panel__title { font-family: "Great Vibes", cursive; color: var(--muted); font-size: 46px; line-height: 1; }
  .details .panel__title { margin-top: 10px; }
  .rsvp .panel__title { margin-top: 12px; font-size: 48px; }
  .flourish { display: block; margin: 4px auto 0; }
  .label { font-family: "Great Vibes", cursive; font-size: 36px; line-height: 1; margin-top: 14px; }
  .label--location { margin-top: 16px; }
  .line { font-size: 15px; line-height: 30px; }
  .first-line { margin-top: 10px; }
  .reception { font-style: italic; font-weight: 700; font-size: 19px; margin-top: 30px; letter-spacing: 0.5px; }
  .rsvp__deadline { font-size: 15px; margin-top: 10px; }
  .choices { position: absolute; left: 140px; top: 168px; list-style: none; text-align: left; }
  .choice { display: flex; align-items: center; font-size: 16px; height: 40px; letter-spacing: 0.5px; }
  .choice svg { margin-right: 12px; }

  .concept-caption { position: absolute; left: 254px; top: 912px;
    font-family: "Questrial", sans-serif; font-size: 38px; color: var(--ink); letter-spacing: 1px; }
</style>
</head>
<body>
<main class="canvas">
  <section class="card" aria-label="Save the date card"></section>

  <div class="block groom-left-art" role="img" aria-label="Illustration of the first groom in a dark suit and sunglasses"></div>
  <div class="block name-bar name-bar--left"><span class="name name--left">Ethan Cole</span></div>

  <header class="block headline">
    <span class="headline__small">Are Getting</span>
    <span class="headline__big">Married</span>
  </header>

  <div class="block save-date">Save The Date</div>
  <div class="block date-band">21-03-2020</div>

  <div class="block couple-heart-art" role="img" aria-label="Heart badge with a small illustration of the two grooms"></div>
  <div class="block name-bar name-bar--right"><span class="name name--right">Julian Reyes</span></div>
  <div class="block groom-right-art" role="img" aria-label="Illustration of the second groom in a grey shirt and light jeans"></div>

  <section class="block panel details">
    <h2 class="panel__title">Details</h2>
    <svg class="flourish" width="300" height="10" viewBox="0 0 300 10" aria-hidden="true">
      <line x1="0" y1="5" x2="300" y2="5" stroke="#6c7384" stroke-width="1"/>
    </svg>
    <h3 class="label">Time</h3>
    <p class="line first-line">Satur Day, March 21, 2020</p>
    <p class="line">4 o' Clock the afternoon</p>
    <h3 class="label label--location">Location</h3>
    <p class="line first-line">Lumen Hotel, Banquet Hall</p>
    <p class="line">48 Orchid Lane, Bangkok</p>
    <p class="reception">Reception to follow</p>
  </section>

  <div class="block rose-art" role="img" aria-label="Watercolour pink roses on red"></div>

  <section class="block panel rsvp">
    <h2 class="panel__title">RSVP</h2>
    <svg class="flourish" width="300" height="10" viewBox="0 0 300 10" aria-hidden="true">
      <line x1="0" y1="5" x2="300" y2="5" stroke="#6c7384" stroke-width="1"/>
    </svg>
    <p class="rsvp__deadline">Before 15th of March, 2020</p>
    <ul class="choices">
      <li class="choice"><svg width="14" height="14" viewBox="0 0 14 14" aria-hidden="true"><circle cx="7" cy="7" r="5.5" fill="none" stroke="#ffffff" stroke-width="1.2"/></svg>Joyfully accept</li>
      <li class="choice"><svg width="14" height="14" viewBox="0 0 14 14" aria-hidden="true"><circle cx="7" cy="7" r="5.5" fill="none" stroke="#ffffff" stroke-width="1.2"/></svg>Regretfully decline</li>
    </ul>
  </section>
  <div class="block rose-faint-art" role="img" aria-label="Faint rose sketch decoration"></div>

  <p class="concept-caption">3RD CONCEPT - 5in X 7in</p>
</main>
</body>
</html>
```